Mission Vision and Values Infographic

We are a healthcare organisation and would like to create a graphic which showcases our Mission, Vision and Values in a clear and beautiful manner.

Attached is:

* Our mission vision and values.
* Style Guide
* Examples of other designs found on the web
* Logo

Your design should be Simple, Clear, Professional and Beautiful.

If you prefer, you can submit a Basic design to start off with for initial feedback before then refining in a future submission. Please check back in the comments section as I will be providing additional general remarks if needed.

The design needs to be created in a tool which will then allow us to modify it in the future…. Ideally either Adobe InDesign, Adobe Illustrator or Adobe Photoshop. Vector is preferred.

All together, the whole design needs to be:

* Printable on one sheet of A3 size paper (to go on our wall)
* Be able to go on a webpage

So there might be slight variations for bigger and smaller displays. For example, the A3 Page will have all three - Mission, Vision and Values + Logo together. The version for a webpage might be separated into 3 parts to make it easier to show on a webpage.

Good luck and happy designing

```html
<!DOCTYPE html>
<html lang="en">
<head>
<meta charset="utf-8">
<title>Vision, Mission and Values</title>
<link rel="stylesheet" href="https://fonts.googleapis.com/css2?family=Open+Sans:wght@400;600;700&family=Arimo:wght@400&display=swap">
<style>
  :root {
    --vision-blue: #114c8e;
    --mission-blue: #29a8e0;
    --red: #e3232a;
    --sky: #6ccadb;
    --purple: #b34a9f;
    --navy: #34499b;
    --green: #6ab444;
    --yellow: #ebe61f;
    --panel: #f2f3f5;
    --connector: #dcdde0;
    --ink: #4a4a4a;
    --white: #ffffff;
  }
  * { box-sizing: border-box; margin: 0; padding: 0; }
  html, body { width: 848px; height: 1200px; overflow: hidden; background: var(--white); }
  .page { position: relative; width: 848px; height: 1200px; font-family: "Open Sans", sans-serif; }

  .statement { color: var(--white); text-align: center; padding: 16px 70px 0; }
  .statement h2 { font-weight: 700; font-size: 27px; line-height: 36px; margin-bottom: 8px; }
  .statement p { font-family: "Arimo", sans-serif; font-size: 18.5px; line-height: 24px; }
  .vision { background: var(--vision-blue); height: 178px; }
  .mission { background: var(--mission-blue); height: 175px; }

  .map-wash { position: absolute; left: 110px; top: 385px; width: 300px; height: 175px;
    background: radial-gradient(ellipse at center, #eef1f4 0%, rgba(255,255,255,0) 70%); }
  .hex-row { position: absolute; left: 0; top: 395px; }

  .value-card { position: absolute; width: 354px; height: 104px; }
  .value-card .panel { position: absolute; left: 50px; top: 0; width: 284px; height: 104px; background: var(--panel); }
  .value-card .bar { position: absolute; right: 0; top: 0; width: 20px; height: 104px; }
  .value-card .badge { position: absolute; left: 0; top: 6px; }
  .value-card h3 { position: absolute; left: 100px; top: 22px; font-size: 11px; font-weight: 700; }
  .value-card p { position: absolute; left: 100px; top: 40px; width: 225px; font-size: 8.6px; line-height: 10px; color: var(--ink); }
  .value-card p.lead { top: 40px; }
  .connector { position: absolute; width: 8px; height: 16px; background: var(--connector); }
</style>
</head>
<body>
<div class="page">
  <section class="statement vision">
    <h2>Our Vision</h2>
    <p>Individuals of all abilities will have the opportunity to achieve their therapy goals by accessing gold standard services, so they may confidently participate in the wider community where they will be understood, supported and embraced for their individuality</p>
  </section>
  <section class="statement mission">
    <h2>Our Mission</h2>
    <p>At Harbourside Speech Clinic we strive to ensure our clients and families have access to high quality, evidence-based intervention from a passionate and professional team to improve and develop individual functional skills that contribute to successful participation in the community</p>
  </section>

  <div class="map-wash" role="img" aria-label="Faint world map behind the values row"></div>

  <svg class="hex-row" width="848" height="155" viewBox="0 0 848 155" font-family="Open Sans, sans-serif" font-weight="700" font-size="10.5" fill="#fff" text-anchor="middle">
    <defs>
      <filter id="lift" x="-20%" y="-20%" width="140%" height="140%"><feDropShadow dx="0" dy="1" stdDeviation="2" flood-opacity="0.25"/></filter>
      <g id="hexframe">
        <polygon points="0,0 46,26 46,124 0,150 -46,124 -46,26"/>
        <polygon fill="#fff" filter="url(#lift)" points="0,17 52,45 52,105 0,133 -52,105 -52,45"/>
      </g>
    </defs>
    <g transform="translate(103,2)" fill="var(--red)"><use href="#hexframe"/>
      <polygon points="0,30 39,52 39,98 0,120 -39,98 -39,52"/>
      <circle cx="0" cy="48" r="8" fill="none" stroke="#fff" stroke-width="2"/><path d="M-5 55 l-3 10 5 -3 3 4 M5 55 l3 10 -5 -3 -3 4" fill="none" stroke="#fff" stroke-width="2"/>
      <text y="89" fill="#fff">QUALITY</text></g>
    <g transform="translate(230,2)" fill="var(--sky)"><use href="#hexframe"/>
      <polygon points="0,30 39,52 39,98 0,120 -39,98 -39,52"/>
      <path d="M0 66 V42 M-5 47 L0 41 5 47 M0 56 L-9 46 M0 56 L9 46" fill="none" stroke="#fff" stroke-width="2.5"/>
      <text y="91" fill="#fff">FLEXIBILITY</text></g>
    <g transform="translate(358,2)" fill="var(--purple)"><use href="#hexframe"/>
      <polygon points="0,30 39,52 39,98 0,120 -39,98 -39,52"/>
      <circle cx="-2" cy="45" r="5" fill="#fff"/><path d="M-12 62 q10 -14 20 0 z" fill="#fff"/><path d="M6 52 l6 2 v5 q0 4 -6 6 q-6 -2 -6 -6 v-5 z" fill="#fff" stroke="var(--purple)"/>
      <text y="91" fill="#fff">INTEGRITY</text></g>
    <g transform="translate(486,2)" fill="var(--navy)"><use href="#hexframe"/>
      <polygon points="0,30 39,52 39,98 0,120 -39,98 -39,52"/>
      <g fill="none" stroke="#fff" stroke-width="1.5"><circle cx="-7" cy="44" r="4"/><circle cx="7" cy="44" r="4"/><circle cx="0" cy="50" r="4"/><path d="M-9 66 v-6 q9 -7 18 0 v6"/></g>
      <text y="91" fill="#fff">DICERSITY</text></g>
    <g transform="translate(614,2)" fill="var(--green)"><use href="#hexframe"/>
      <polygon points="0,30 39,52 39,98 0,120 -39,98 -39,52"/>
      <path d="M-8 66 v-6 q-6 -6 -3 -13 q5 -9 14 -5 q6 4 4 10 l3 5 h-3 v5 h-5 v4" fill="none" stroke="#fff" stroke-width="2"/><path d="M-4 50 l3 3 5 -6" fill="none" stroke="#fff" stroke-width="2"/>
      <text y="91" fill="#fff">POSITIVITY</text></g>
    <g transform="translate(742,2)" fill="var(--yellow)"><use href="#hexframe"/>
      <polygon points="0,30 39,52 39,98 0,120 -39,98 -39,52"/>
      <path d="M-4 62 v-4 q-6 -4 -6 -10 a10 10 0 0 1 20 0 q0 6 -6 10 v4 z M-3 66 h6" fill="none" stroke="#fff" stroke-width="1.8"/>
      <text y="91" fill="#fff">CREATIVITY</text></g>
  </svg>

  <!-- connectors -->
  <div class="connector" style="left:96px; top:770px;"></div>
  <div class="connector" style="left:96px; top:888px;"></div>
  <div class="connector" style="left:469px; top:770px;"></div>
  <div class="connector" style="left:469px; top:888px;"></div>

  <article class="value-card" style="left:55px; top:666px;">
    <div class="panel"></div><div class="bar" style="background:var(--red)"></div>
    <svg class="badge" width="92" height="92" viewBox="0 0 92 92"><path d="M46 0 A46 46 0 0 0 46 92" fill="var(--red)"/><circle cx="46" cy="46" r="39" fill="#fff"/><circle cx="46" cy="46" r="34" fill="var(--red)"/>
      <circle cx="46" cy="39" r="11" fill="none" stroke="#fff" stroke-width="2.5"/><text x="46" y="44" fill="#fff" font-size="12" font-weight="700" text-anchor="middle" font-family="Open Sans, sans-serif">1</text><path d="M40 49 l-4 13 6 -3 3 5 M52 49 l4 13 -6 -3 -3 5" fill="none" stroke="#fff" stroke-width="2.5"/></svg>
    <h3 style="color:var(--red)">QUALITY</h3>
    <p>We strive for excellence through evidence based practice,self-reflection, feedback and a continuous commitment to improvement and discovery both professionally and personally.</p>
  </article>

  <article class="value-card" style="left:428px; top:666px;">
    <div class="panel"></div><div class="bar" style="background:var(--sky)"></div>
    <svg class="badge" width="92" height="92" viewBox="0 0 92 92"><path d="M46 0 A46 46 0 0 0 46 92" fill="var(--sky)"/><circle cx="46" cy="46" r="39" fill="#fff"/><circle cx="46" cy="46" r="34" fill="#62b7c6"/>
      <path d="M46 66 V28 M39 35 L46 27 53 35 M46 52 L32 38 M46 52 L60 38 M30 44 V37 H37 M62 44 V37 H55" fill="none" stroke="#fff" stroke-width="3.5"/></svg>
    <h3 style="color:var(--sky)">FLEXIBILITY</h3>
    <p>We are flexible in our problem solving and offer options and solutions for our families and team wherever we reasonably can.</p>
  </article>

  <article class="value-card" style="left:55px; top:784px;">
    <div class="panel"></div><div class="bar" style="background:var(--purple)"></div>
    <svg class="badge" width="92" height="92" viewBox="0 0 92 92"><path d="M46 0 A46 46 0 0 0 46 92" fill="var(--purple)"/><circle cx="46" cy="46" r="39" fill="#fff"/><circle cx="46" cy="46" r="34" fill="var(--purple)"/>
      <circle cx="42" cy="36" r="9" fill="#fff"/><path d="M26 64 q16 -24 32 0 z" fill="#fff"/><path d="M56 48 l9 3 v7 q0 6 -9 9 q-9 -3 -9 -9 v-7 z" fill="#fff" stroke="var(--purple)" stroke-width="2"/></svg>
    <h3 style="color:var(--purple)">INTEGRITY</h3>
    <p>We care for and respect the needs and well-being of our families, our team and ourselves. We encourage openness, trust and honest communication at all times.</p>
  </article>

  <article class="value-card" style="left:428px; top:784px;">
    <div class="panel"></div><div class="bar" style="background:var(--green)"></div>
    <svg class="badge" width="92" height="92" viewBox="0 0 92 92"><path d="M46 0 A46 46 0 0 0 46 92" fill="var(--green)"/><circle cx="46" cy="46" r="39" fill="#fff"/><circle cx="46" cy="46" r="34" fill="var(--green)"/>
      <path d="M34 68 v-9 q-9 -8 -5 -19 q7 -14 22 -8 q9 5 7 15 l5 8 h-5 v7 h-7 v6" fill="none" stroke="#fff" stroke-width="3"/><path d="M38 43 l5 5 8 -9" fill="none" stroke="#fff" stroke-width="3"/></svg>
    <h3 style="color:var(--green)">POSITIVITY</h3>
    <p>We lead ourselves 'above the line' choosing to adopt a positive, accountable and solution-focused mindset.</p>
  </article>

  <article class="value-card" style="left:55px; top:902px;">
    <div class="panel"></div><div class="bar" style="background:var(--navy)"></div>
    <svg class="badge" width="92" height="92" viewBox="0 0 92 92"><path d="M46 0 A46 46 0 0 0 46 92" fill="var(--navy)"/><circle cx="46" cy="46" r="39" fill="#fff"/><circle cx="46" cy="46" r="34" fill="var(--navy)"/>
      <g fill="none" stroke="#fff" stroke-width="2"><circle cx="34" cy="32" r="6"/><circle cx="58" cy="32" r="6"/><circle cx="46" cy="42" r="6"/><path d="M24 58 v-8 q10 -10 20 -6 M68 58 v-8 q-10 -10 -20 -6 M34 68 v-10 q12 -10 24 0 v10"/></g></svg>
    <h3 style="color:var(--navy)">DICERSITY</h3>
    <p>We embed diversity by recognising, respecting and appreciating differences in our families and our team.</p>
  </article>

  <article class="value-card" style="left:428px; top:902px;">
    <div class="panel"></div><div class="bar" style="background:var(--yellow)"></div>
    <svg class="badge" width="92" height="92" viewBox="0 0 92 92"><path d="M46 0 A46 46 0 0 0 46 92" fill="var(--yellow)"/><circle cx="46" cy="46" r="39" fill="#fff"/><circle cx="46" cy="46" r="34" fill="#dcd91d"/>
      <path d="M40 62 v-6 q-10 -6 -10 -17 a16 16 0 0 1 32 0 q0 11 -10 17 v6 z M40 67 h12 M42 71 h8" fill="none" stroke="#fff" stroke-width="2.5"/><path d="M41 45 q5 -8 10 0" fill="none" stroke="#fff" stroke-width="2"/></svg>
    <p class="lead">We are innovative and collaborative, constantly working towards new and improved ways to support our clients, families and our team.</p>
  </article>
</div>
</body>
</html>
```